Project Title:
Dental Implant Overdenture Flyer (Retirement Village Target)
Objective:
Create a clean, trustworthy, and reassuring flyer aimed at older adults (60–85 years old) who struggle with loose dentures. The goal is to educate them about implant-retained “clip-on” dentures and encourage them to book a consultation.
Tone & Feel:
Warm, caring, non-intimidating
Premium but not “salesy”
Medical but easy to understand
Focus on improving quality of life (confidence, eating, comfort)
Target Audience:
Retirees / pensioners
Existing denture wearers
People frustrated with loose or uncomfortable dentures
Key Message:
“You don’t have to live with loose dentures anymore.”
Design Style:
Clean, minimal, modern
Soft colours (blues, greens, warm neutrals)
Easy-to-read large font
High contrast for older eyes
Avoid clutter
Imagery Suggestions:
Smiling older adults (natural, not stocky/overly staged)
Before/after lifestyle (eating, laughing, socialising)
Simple diagram showing denture clipping onto implants
Avoid graphic surgical images
Layout Suggestions:
A5 or DL flyer
Clear sections with headings
Icons for benefits
Strong call-to-action at bottom
HEADLINE (big and bold)
Tired of Loose Dentures?
Discover Secure “Clip-On” Teeth
🔹 PROBLEM SECTION
Do your dentures:
Slip or move when eating?
Make it hard to chew certain foods?
Feel uncomfortable or loose?
Affect your confidence when speaking or smiling?
You’re not alone — and there is a better solution.
🔹 SOLUTION SECTION
Implant-Retained “Clip-On” Dentures
We can secure your denture using just 2 dental implants, allowing your teeth to:
✔ Stay firmly in place
✔ Improve your ability to eat
✔ Feel more comfortable
✔ Boost your confidence
🔹 SIMPLE EXPLANATION (very important)
Small titanium implants are gently placed in the jaw.
Your denture then clips securely onto them, stopping movement.
🔹 PRICE SECTION (highlight this clearly)
$12,000
Includes:
2 dental implants
A brand new custom overdenture
Does not include sedation or extractions (if needed)
🔹 SEDATION
Sedation is available for comfort.
If you hold a pensioner card, you may receive a significant Vantacor rebate, often resulting in minimal out-of-pocket costs for sedation.
🔹 TRUST / REASSURANCE
Experienced implant clinician
Gentle, patient-focused care
Modern technology and techniques
🔹 CALL TO ACTION (VERY IMPORTANT)
Book a Free Consultation
📞 Call: 08 9351 4276
🌐 Visit: www.bravonclinic.com.au
📍 Located near Tallowmere shopping centre
🔹 OPTIONAL TAGLINE
Eat Better. Feel Better. Smile with Confidence Again.
Please include some photos to illustrate what a clip on denture looks like with two implants.

```html
<!DOCTYPE html>
<html lang="en">
<head>
<meta charset="utf-8">
<title>Bravon Clinic – Clip-On Dentures Flyer</title>
<link href="https://fonts.googleapis.com/css2?family=Poppins:wght@400;500;600;700;800&display=swap" rel="stylesheet">
<style>
:root{
  --navy:#0e1b3d;
  --blue:#1b5f98;
  --blue-deep:#1a5590;
  --teal:#14a9bb;
  --teal-dark:#0f8fa8;
  --panel:#d5e7eb;
  --white:#ffffff;
  --rule:#b9c3cc;
  --text:#1c2235;
}
*{margin:0;padding:0;box-sizing:border-box}
html,body{width:935px;height:1200px;overflow:hidden;background:var(--white)}
body{font-family:"Poppins",sans-serif;color:var(--text)}
.flyer{position:relative;width:935px;height:1200px;overflow:hidden;background:var(--white)}
.header{position:absolute;left:0;top:0;width:935px;height:436px;background:linear-gradient(180deg,var(--blue-deep) 0%,#17709f 60%,var(--teal-dark) 100%)}
.brand{position:absolute;left:58px;top:62px;display:flex;align-items:center;gap:12px;color:var(--white);font-weight:600;font-size:22px;letter-spacing:3px}
.brand-dot{width:18px;height:18px;border-radius:50%;background:var(--white)}
.headline{position:absolute;left:57px;top:190px;font-weight:800;font-size:44px;line-height:42px;color:var(--navy);letter-spacing:-0.5px}
.subhead{position:absolute;left:57px;top:290px;font-weight:800;font-size:35px;line-height:40px;color:var(--white)}
.photo{position:absolute;left:436px;top:40px;width:499px;height:396px;background:linear-gradient(160deg,#6f9fc4 0%,#b9c7cf 45%,#e8d9a8 70%,#7e93b0 100%);opacity:.9}
.problem-panel{position:absolute;left:58px;top:436px;width:402px;height:545px;background:var(--panel);border-radius:0 0 0 14px;overflow:hidden}
.panel-title{font-weight:800;font-size:20px;line-height:26px;color:var(--navy);margin:26px 0 8px 40px}
.numbered{list-style:none;margin-left:40px}
.numbered li{display:flex;gap:10px;font-size:16.5px;line-height:20px;margin-bottom:6px}
.num{flex:none;width:19px;height:19px;border-radius:50%;background:var(--blue);color:var(--white);font-size:12px;font-weight:700;display:flex;align-items:center;justify-content:center;margin-top:1px}
.reassure{margin:4px 0 0 49px;font-weight:700;font-size:16.5px;line-height:20px;color:var(--blue)}
.solution-title{font-weight:800;font-size:20px;line-height:26px;color:var(--navy);margin:16px 0 6px 52px}
.solution-lead{margin-left:49px;font-weight:700;font-size:16px;line-height:20px;color:var(--blue)}
.ticks{list-style:none;margin:8px 0 0 49px}
.ticks li{display:flex;align-items:center;gap:10px;font-size:16.5px;line-height:22px;margin-bottom:6px}
.tick{flex:none;width:14px;height:14px}
.price-block{position:absolute;left:488px;top:450px;width:392px}
.price-row{display:flex;align-items:flex-start;gap:12px}
.price{font-weight:600;font-size:44px;line-height:50px;color:var(--navy);letter-spacing:-1px}
.price sup{font-size:20px;vertical-align:top;position:relative;top:4px}
.includes-tag{margin-top:14px;height:28px;display:flex;align-items:center;padding:0 34px 0 8px;background:var(--blue);color:var(--white);font-weight:700;font-size:16px;clip-path:polygon(0 0,100% 0,86% 50%,100% 100%,0 100%)}
.includes{display:flex;margin-top:10px}
.include{display:flex;gap:8px;font-size:17px;line-height:21px;padding-left:6px}
.include + .include{border-left:1px solid var(--rule);margin-left:14px;padding-left:14px}
.include .tick{margin-top:4px}
.exclusions{margin:14px 0 0 8px;font-size:16px;line-height:20px}
.exclusions span{color:var(--teal)}
.rule{height:1.5px;background:var(--rule);margin:10px 0 0 0}
.sedation-title{font-weight:800;font-size:21px;line-height:27px;color:var(--navy);margin:12px 0 4px 8px}
.sedation-text{margin-left:8px;font-size:16.5px;line-height:21px}
.trust{list-style:none;margin-top:14px}
.trust li{display:flex;align-items:center;gap:14px;font-size:17px;margin-bottom:12px}
.trust-icon{flex:none;width:42px;height:42px;border-radius:50%;background:var(--navy);display:flex;align-items:center;justify-content:center}
.cta{position:absolute;left:47px;top:1004px;width:760px;height:60px}
.cta-button{position:absolute;left:52px;top:4px;width:395px;height:52px;border-radius:0 26px 26px 0;background:var(--teal);color:var(--white);font-size:23px;display:flex;align-items:center;padding-left:47px}
.cta-button b{font-weight:800;margin:0 6px}
.megaphone{position:absolute;left:0;top:0}
.contacts{position:absolute;left:58px;top:1080px;width:540px;display:grid;grid-template-columns:260px 280px;row-gap:12px;font-size:16.5px;line-height:19px;color:var(--navy);font-weight:500}
.contact{display:flex;gap:8px}
.contact svg{flex:none;margin-top:1px}
.diagram{position:absolute;left:620px;top:957px;width:256px;height:182px;background:linear-gradient(180deg,#f3f5f7 0%,#f2b6b0 45%,#e27b78 62%,#e9dcc3 85%,#b9dce4 100%)}
</style>
</head>
<body>
<div class="flyer">
  <header class="header">
    <div class="brand"><span class="brand-dot"></span>BRAVON CLINIC</div>
    <h1 class="headline">TIRED OF LOOSE<br>DENTURES?</h1>
    <h2 class="subhead">DISCOVER SECURE<br>“CLIP-ON” TEETH</h2>
    <div class="photo" role="img" aria-label="Photo of a smiling older couple standing together"></div>
  </header>

  <section class="problem-panel">
    <h3 class="panel-title">DO YOUR DENTURES</h3>
    <ol class="numbered">
      <li><span class="num">1</span>Slip or move when eating?</li>
      <li><span class="num">2</span>Make it hard to chew<br>certain foods?</li>
      <li><span class="num">3</span>Feel uncomfortable or loose?</li>
      <li><span class="num">4</span>Affect your confidence when<br>speaking or smiling?</li>
    </ol>
    <p class="reassure">You’re not alone<br>and there is a better solution.</p>
    <h3 class="solution-title">IMPLANT-RETAINED<br>“CLIP-ON” DENTURES</h3>
    <p class="solution-lead">We can secure your denture<br>using just 2 dental implants,<br>allowing your teeth to:</p>
    <ul class="ticks">
      <li><svg class="tick" viewBox="0 0 14 14"><circle cx="7" cy="7" r="7" fill="#1b5f98"/><path d="M4 7.2l2 2 4-4.2" stroke="#fff" stroke-width="1.6" fill="none"/></svg>Stay firmly in place</li>
      <li><svg class="tick" viewBox="0 0 14 14"><circle cx="7" cy="7" r="7" fill="#1b5f98"/><path d="M4 7.2l2 2 4-4.2" stroke="#fff" stroke-width="1.6" fill="none"/></svg>Improve your ability to eat</li>
      <li><svg class="tick" viewBox="0 0 14 14"><circle cx="7" cy="7" r="7" fill="#1b5f98"/><path d="M4 7.2l2 2 4-4.2" stroke="#fff" stroke-width="1.6" fill="none"/></svg>Feel more comfortable</li>
      <li><svg class="tick" viewBox="0 0 14 14"><circle cx="7" cy="7" r="7" fill="#1b5f98"/><path d="M4 7.2l2 2 4-4.2" stroke="#fff" stroke-width="1.6" fill="none"/></svg>Boost your confidence</li>
    </ul>
  </section>

  <section class="price-block">
    <div class="price-row">
      <div class="price"><sup>$</sup>12,000</div>
      <div class="includes-tag">INCLUDES</div>
    </div>
    <div class="includes">
      <div class="include"><svg class="tick" viewBox="0 0 14 14"><circle cx="7" cy="7" r="7" fill="#1b5f98"/><path d="M4 7.2l2 2 4-4.2" stroke="#fff" stroke-width="1.6" fill="none"/></svg><span>2 dental<br>implants</span></div>
      <div class="include"><svg class="tick" viewBox="0 0 14 14"><circle cx="7" cy="7" r="7" fill="#1b5f98"/><path d="M4 7.2l2 2 4-4.2" stroke="#fff" stroke-width="1.6" fill="none"/></svg><span>A brand new custom<br>overdenture</span></div>
    </div>
    <p class="exclusions">Does not include sedation or extractions<br><span>(if needed)</span></p>
    <div class="rule"></div>
    <h3 class="sedation-title">SEDATION IS AVAILABLE<br>FOR COMFORT</h3>
    <p class="sedation-text">If you hold a pensioner card, you may receive a significant Vantacor rebate, often resulting in minimal out-of-pocket costs for sedation.</p>
    <div class="rule" style="margin-top:16px"></div>
    <ul class="trust">
      <li><span class="trust-icon"><svg width="20" height="22" viewBox="0 0 20 22"><path d="M3 2c3-2 5 0 7 0s4-2 7 0c2 2 1 6-1 7H4C2 8 1 4 3 2z" fill="#fff"/><rect x="7" y="11" width="6" height="2" fill="#fff"/><rect x="7.5" y="14" width="5" height="2" fill="#fff"/><path d="M8 17h4l-2 4z" fill="#fff"/></svg></span>Experienced implant clinician</li>
      <li><span class="trust-icon"><svg width="22" height="22" viewBox="0 0 22 22"><circle cx="11" cy="6" r="4" fill="#fff"/><path d="M2 16c3 0 5-3 9-3s6 3 9 3v3H2z" fill="#fff"/></svg></span>Gentle, patient-focused care</li>
      <li><span class="trust-icon"><svg width="22" height="20" viewBox="0 0 22 20"><rect x="1" y="1" width="20" height="18" rx="2" fill="none" stroke="#fff" stroke-width="1.6"/><rect x="5" y="5" width="3" height="10" fill="#fff"/><rect x="10" y="5" width="2" height="10" fill="#fff"/><rect x="14" y="5" width="3" height="10" fill="#fff"/></svg></span>Modern technology and techniques</li>
    </ul>
  </section>

  <div class="cta">
    <div class="cta-button">Book a <b>FREE</b> Consultation</div>
    <svg class="megaphone" width="84" height="64" viewBox="0 0 84 64">
      <path d="M10 24h14l30-18v52L24 40H10z" fill="#2f6fb0"/>
      <rect x="4" y="24" width="10" height="16" rx="2" fill="#1b4f86"/>
      <path d="M18 40l6 20h8l-4-20z" fill="#1b4f86"/>
      <path d="M54 6c6 6 6 46 0 52" stroke="#9fd3e6" stroke-width="5" fill="none"/>
      <path d="M66 20l10-6M68 32h12M66 44l10 6" stroke="#14a9bb" stroke-width="3" stroke-linecap="round"/>
    </svg>
  </div>

  <div class="contacts">
    <div class="contact"><svg width="16" height="16" viewBox="0 0 16 16"><circle cx="8" cy="8" r="8" fill="#14a9bb"/><path d="M5 4l2 2-1 1c.5 1.5 1.5 2.5 3 3l1-1 2 2-1.5 1.5C7 12 4 9 3.5 5.5z" fill="#fff"/></svg>08 9351 4276</div>
    <div class="contact"><svg width="16" height="16" viewBox="0 0 16 16"><circle cx="8" cy="8" r="8" fill="#14a9bb"/><rect x="4" y="5" width="8" height="6" fill="#fff"/><path d="M4 5l4 3.5L12 5" stroke="#14a9bb" fill="none"/></svg>info@bravonclinic.com.au</div>
    <div class="contact"><svg width="16" height="16" viewBox="0 0 16 16"><circle cx="8" cy="8" r="8" fill="#14a9bb"/><path d="M8 3.5a3 3 0 0 1 3 3c0 2.2-3 5.5-3 5.5S5 8.7 5 6.5a3 3 0 0 1 3-3z" fill="#fff"/><circle cx="8" cy="6.5" r="1" fill="#14a9bb"/></svg><span>Located near Tallowmere<br>shopping centre</span></div>
    <div class="contact"><svg width="16" height="16" viewBox="0 0 16 16"><circle cx="8" cy="8" r="8" fill="#14a9bb"/><circle cx="8" cy="8" r="4.5" fill="none" stroke="#fff" stroke-width="1.2"/><path d="M3.5 8h9M8 3.5c-2 2.5-2 6.5 0 9M8 3.5c2 2.5 2 6.5 0 9" stroke="#fff" stroke-width="1" fill="none"/></svg>www.bravonclinic.com.au</div>
  </div>

  <div class="diagram" role="img" aria-label="Illustration of teeth in the gum showing a natural tooth, a tooth cross-section and a dental implant"></div>
</div>
</body>
</html>
```